Brindlemark Services Ltd

I'd like to create a company letterhead for the attached logo in word format.

I'd like to emphasis the icon in large translucent state from the left corner and ensure that the letterhead colouring matches the colour palette of the current logo with a contrast so it's clear to see. I've attached a copy of our sister company page on the app for reference.

```html
<!DOCTYPE html>
<html lang="en">
<head>
<meta charset="utf-8">
<title>Brindlemark Services Ltd – Letterhead</title>
<link rel="stylesheet" href="https://fonts.googleapis.com/css2?family=Montserrat:wght@400;500&display=swap">
<style>
  :root {
    --brand-teal: #00b8a2;
    --brand-teal-faint: rgba(0, 184, 162, 0.07);
    --paper: #ffffff;
    --backdrop: #e6e6e6;
  }
  * { margin: 0; padding: 0; box-sizing: border-box; }
  html, body {
    width: 1200px;
    height: 1200px;
    overflow: hidden;
    background: var(--backdrop);
    font-family: "Montserrat", sans-serif;
  }
  .letterhead {
    position: absolute;
    left: 175px;
    top: 50px;
    width: 850px;
    height: 1100px;
    background: var(--paper);
    box-shadow: 0 2px 10px rgba(0,0,0,0.12);
    overflow: hidden;
  }
  .corner-watermark {
    position: absolute;
    left: -300px;
    top: 200px;
    width: 680px;
    height: 680px;
    border-radius: 50%;
    background: var(--brand-teal-faint);
    z-index: 0;
  }
  .letterhead-header { position: relative; z-index: 1; }
  .brand {
    position: absolute;
    left: 33px;
    top: 53px;
    width: 240px;
    display: flex;
    flex-direction: column;
    align-items: center;
  }
  .brand-dot {
    width: 74px;
    height: 74px;
    border-radius: 50%;
    background: var(--brand-teal);
  }
  .brand-name {
    margin-top: 18px;
    font-size: 16.5px;
    font-weight: 500;
    color: var(--brand-teal);
    white-space: nowrap;
  }
  .contact {
    position: absolute;
    right: 63px;
    top: 54px;
    text-align: right;
    color: var(--brand-teal);
    font-style: normal;
    font-size: 13.5px;
    line-height: 18px;
    font-weight: 400;
    white-space: nowrap;
  }
  .contact-line {
    display: flex;
    justify-content: flex-end;
    align-items: center;
    gap: 6px;
  }
  .contact-line svg {
    width: 10px;
    height: 10px;
    flex: none;
  }
  .contact-divider {
    display: inline-block;
    width: 10px;
    height: 1px;
    background: var(--brand-teal);
    margin: 8px 0 7px;
  }
  .office-name {
    font-size: 16px;
    line-height: 20px;
    letter-spacing: 0.3px;
  }
  .side-accent {
    position: absolute;
    right: 0;
    top: 56px;
    width: 7px;
    height: 119px;
    background: var(--brand-teal);
  }
  .footer-band {
    position: absolute;
    left: 0;
    bottom: 0;
    width: 100%;
    height: 35px;
    background: var(--brand-teal);
    z-index: 1;
  }
  .footer-dot {
    position: absolute;
    left: 50%;
    bottom: 0;
    width: 46px;
    height: 46px;
    margin-left: -23px;
    margin-bottom: -6px;
    border-radius: 50%;
    background: var(--paper);
  }
</style>
</head>
<body>
  <main class="letterhead">
    <div class="corner-watermark" aria-hidden="true"></div>

    <header class="letterhead-header">
      <div class="brand">
        <div class="brand-dot"></div>
        <div class="brand-name">Brindlemark Services Ltd</div>
      </div>

      <address class="contact">
        <div class="contact-line">01632 960 418
          <svg viewBox="0 0 10 10" aria-hidden="true"><path d="M2.2 1 L3.6 1 L4.2 3 L3.2 3.8 Q4 5.8 6.2 6.8 L7 5.8 L9 6.4 L9 7.8 Q9 9 7.8 9 Q1 8.4 1 2.2 Q1 1 2.2 1 Z" fill="none" stroke="currentColor" stroke-width="1.1"/></svg>
        </div>
        <div class="contact-line">hello@brindlemark.co.uk
          <svg viewBox="0 0 10 10" aria-hidden="true"><rect x="1" y="2" width="8" height="6" fill="none" stroke="currentColor" stroke-width="1.1"/><path d="M1 2.5 L5 5.5 L9 2.5" fill="none" stroke="currentColor" stroke-width="1.1"/></svg>
        </div>
        <div class="contact-line">www.brindlemark.co.uk
          <svg viewBox="0 0 10 10" aria-hidden="true"><circle cx="5" cy="5" r="4" fill="none" stroke="currentColor" stroke-width="1"/><ellipse cx="5" cy="5" rx="1.8" ry="4" fill="none" stroke="currentColor" stroke-width="0.8"/><path d="M1 5 H9 M1.6 3 H8.4 M1.6 7 H8.4" stroke="currentColor" stroke-width="0.7"/></svg>
        </div>
        <span class="contact-divider"></span>
        <div class="office-name">BRINDLEMARK</div>
        <div>17 Harrowgate Crescent,</div>
        <div>2nd Floor, Dunmoor, DN4 7QX</div>
      </address>

      <div class="side-accent"></div>
    </header>

    <footer class="footer-band">
      <div class="footer-dot"></div>
    </footer>
  </main>
</body>
</html>
```